IT Support Business needs a Flyer Designed

Have just had new logo and business cards made for new business called Byte Harbor, am now in need of a new flyer design. Byte Harbor will be providing home and small business it support.
Updates
Byte Harbor flyer design brief has been uploaded. The contest has also been changed to payment guaranteed.
If you need anymore information please feel free to contact myself.
Project Deadline Extended
Reason: I signed up early to take advantage of the artforge 24 hour sale, and was a few days late in providing a design brief. Therefore I am extending the deadline by 2 days, to ensure it lasts for a good 2 weeks.
Have worked on and refined the Design Brief a bit more, hoping it makes it a bit clearer as to what I want on the flyer. If you have any questions please do not hesitate to ask.
I have refined the design brief overnight, after receiving some feedback, please refer to newly uploaded file for this morning. I am hoping it makes things clearer and easier.
Industry/Entity Type
Small Business

```html
<!DOCTYPE html>
<html lang="en">
<head>
<meta charset="utf-8">
<title>Byte Harbor Flyer</title>
<link rel="stylesheet" href="https://fonts.googleapis.com/css2?family=Source+Sans+3:wght@400;600;700&display=swap">
<style>
  :root {
    --brand-blue: #1b6db4;
    --sky: #bfe3f7;
    --frame: #cfd3d7;
    --orange: #f7941d;
    --coral: #ee5a45;
    --ink: #333333;
    --white: #ffffff;
    --paper: #ffffff;
  }
  * { box-sizing: border-box; margin: 0; padding: 0; }
  html, body { width: 779px; height: 1200px; overflow: hidden; background: var(--paper); }
  body { font-family: "Source Sans 3", Arial, sans-serif; color: var(--ink); }
  .flyer { position: relative; width: 779px; height: 1200px; overflow: hidden; background: var(--paper); }

  .brand { position: absolute; top: 50px; left: 0; width: 779px; display: flex; justify-content: center; align-items: center; gap: 16px; }
  .brand-dot { width: 54px; height: 54px; border-radius: 50%; background: var(--brand-blue); }
  .brand-name { font-size: 68px; font-weight: 700; color: var(--brand-blue); letter-spacing: 2px; line-height: 1; }

  .headline { position: absolute; top: 155px; left: 29px; width: 731px; height: 97px; background: var(--brand-blue); border-radius: 48px; color: var(--white); font-size: 33px; font-weight: 400; line-height: 1.1; padding: 0 30px 0 50px; display: flex; align-items: center; }

  .intro { position: absolute; top: 264px; left: 30px; width: 720px; font-size: 20px; line-height: 1.45; }

  .artwork { position: absolute; top: 445px; left: 448px; width: 282px; height: 262px; border-radius: 10px; background: linear-gradient(160deg, var(--frame) 0%, var(--sky) 45%, var(--frame) 100%); }

  .services-tag { position: absolute; top: 372px; left: 0; width: 340px; height: 32px; background: var(--orange); border-radius: 0 16px 16px 0; font-size: 21px; font-weight: 600; color: var(--ink); padding: 2px 0 0 62px; }

  .services { position: absolute; top: 414px; left: 48px; width: 700px; list-style: none; }
  .services li { display: flex; align-items: flex-start; gap: 12px; font-size: 20px; line-height: 1.25; margin-bottom: 14px; }
  .services li:last-child { margin-bottom: 0; }
  .services li .icon { flex: none; width: 28px; height: 28px; border-radius: 4px; background: var(--brand-blue); display: flex; align-items: center; justify-content: center; }
  .services li .icon svg { width: 18px; height: 18px; }

  .coverage { position: absolute; top: 724px; left: 29px; width: 731px; height: 134px; background: var(--orange); border-radius: 67px; font-size: 20px; line-height: 1.4; padding: 0 40px 0 54px; display: flex; align-items: center; }

  .pricing { position: absolute; top: 871px; left: 29px; width: 731px; height: 62px; background: var(--coral); border-radius: 31px; color: var(--white); font-size: 19px; line-height: 1.3; padding: 0 40px 0 56px; display: flex; align-items: center; }

  .cta { position: absolute; top: 955px; left: 40px; width: 699px; text-align: center; color: var(--brand-blue); font-size: 29px; line-height: 1.15; }

  .contact { position: absolute; top: 1031px; left: 195px; width: 390px; height: 130px; background: var(--brand-blue); border-radius: 16px; color: var(--white); font-size: 21px; font-style: normal; line-height: 1.24; padding: 12px 18px; white-space: nowrap; }
</style>
</head>
<body>
<main class="flyer">
  <header class="brand">
    <span class="brand-dot"></span>
    <span class="brand-name">Byte Harbor</span>
  </header>

  <h1 class="headline">Providing solutions for all your computer and technical equipment needs.</h1>

  <p class="intro">With over 15 years experience in the IT sector, Daniel from Byte Harbor provides friendly, reliable and professional service, supporting you to build your skills and knowledge to maximise your IT requirements.</p>

  <div class="artwork" role="img" aria-label="Illustration of a desktop monitor and a laptop"></div>

  <div class="services-tag">Byte Harbor specialises in:</div>

  <ul class="services">
    <li><span class="icon"><svg viewBox="0 0 20 20"><path d="M4 16 L12 8 M11 4 a4 4 0 1 0 5 5" stroke="#fff" stroke-width="2.5" fill="none" stroke-linecap="round"/></svg></span>Computer repair, service, installation and upgrades.</li>
    <li><span class="icon"><svg viewBox="0 0 20 20"><rect x="3" y="2" width="6" height="5" fill="#fff"/><rect x="11" y="13" width="6" height="5" fill="#fff"/><path d="M6 7 V15 H11" stroke="#fff" stroke-width="2" fill="none"/></svg></span>Support to set up and secure your home network.</li>
    <li><span class="icon"><svg viewBox="0 0 20 20"><rect x="3" y="3" width="14" height="14" rx="2" fill="none" stroke="#fff" stroke-width="2"/><circle cx="10" cy="10" r="2.5" fill="#fff"/></svg></span>Sharing the tricks and tips to manage your new operating system.</li>
    <li><span class="icon"><svg viewBox="0 0 20 20"><path d="M10 3 V13 M5 9 L10 14 L15 9 M4 17 H16" stroke="#fff" stroke-width="2.2" fill="none" stroke-linecap="round"/></svg></span>Assistance in installing and configuring new software.</li>
    <li><span class="icon"><svg viewBox="0 0 20 20"><circle cx="10" cy="10" r="7" fill="none" stroke="#fff" stroke-width="2"/><path d="M3 10 H17 M10 3 C6 7 6 13 10 17 M10 3 C14 7 14 13 10 17" stroke="#fff" stroke-width="1.5" fill="none"/></svg></span>Getting you connected online and across social media faster,<br>including Internet, email, VoxLink, FriendHub etc.</li>
    <li><span class="icon"><svg viewBox="0 0 20 20"><ellipse cx="10" cy="5" rx="6" ry="2.5" fill="#fff"/><path d="M4 5 V15 C4 17 16 17 16 15 V5" stroke="#fff" stroke-width="2" fill="none"/></svg></span>Data backup and recovery.</li>
    <li><span class="icon"><svg viewBox="0 0 20 20"><rect x="2" y="4" width="16" height="12" rx="1" fill="none" stroke="#fff" stroke-width="2"/><path d="M5 8 L8 10 L5 12" stroke="#fff" stroke-width="1.8" fill="none"/></svg></span>Tuition in programs and technology.</li>
  </ul>

  <p class="coverage">Our services and expertise extends across PC’s, Laptops, printers, scanners, routers, tablet, mobile phone, cameras, television and arcade consoles, with the ability to work onsite or remotely as required.</p>

  <p class="pricing">Byte Harbor service fees start at $40 per hour however packages and flexible pricing for more complex tasks are available.</p>

  <p class="cta">With no call out fee, talk to Daniel today to solve your IT and technology challenges.</p>

  <address class="contact">
    Phone Daniel on 0491570156<br>
    Email is dmarsh@byteharbor.com.au<br>
    Located in Elmsford, Victoria<br>
    ABN is 12345678901
  </address>
</main>
</body>
</html>
```